Business Card Design Project

We need a redesign of our business card.
We are a Consulting Property Developer called The Kestrel Group
Updates

Thank you all for submissions. Just waiting on managment to decide.

Thank you,

Dorinda

Industry/Entity Type

Business

Requirements
Must have
• we like having the KG a focus in the back ground or on the side
Kestrel is our company colour

the wording - property development
and - premium accommodation

our website www.kestrelgroup-example.com.au

persons name
title

p: 1300 482917 f: 1300 482915 m: 0417593824
PO Box 5817, Brindlevale Qld 4178
e: admin@kestrelgroup-example.com.au

```html
<!DOCTYPE html>
<html lang="en">
<head>
<meta charset="utf-8">
<title>The Kestrel Group – Business Card</title>
<link href="https://fonts.googleapis.com/css2?family=Jost:wght@400;500;600&display=swap" rel="stylesheet">
<style>
  :root {
    --kestrel: #8c0a35;
    --kestrel-deep: #6e0427;
    --kestrel-light: #a3143f;
    --ink-grey: #8a8a8a;
    --rule-grey: #b9b9b9;
    --card-white: #f6f7f8;
    --backdrop: #8f8f8c;
    --white: #ffffff;
  }
  * { box-sizing: border-box; margin: 0; padding: 0; }
  html, body { width: 1200px; height: 774px; overflow: hidden; }
  body {
    background: var(--backdrop);
    font-family: "Jost", "Futura", sans-serif;
    position: relative;
  }
  .card {
    position: absolute;
    top: 222px;
    width: 540px;
    height: 330px;
    overflow: hidden;
    box-shadow: 0 10px 24px rgba(0,0,0,0.25);
  }

  /* ---------- Front ---------- */
  .card-front { left: 50px; background: var(--card-white); }
  .front-brand {
    position: absolute; left: 38px; top: 40px;
    display: flex; align-items: center; gap: 14px;
  }
  .brand-dot {
    width: 46px; height: 46px; border-radius: 50%;
    border: 2px solid var(--kestrel);
  }
  .front-brand .brand-name {
    font-size: 30px; font-weight: 400; color: var(--ink-grey);
    letter-spacing: -0.3px;
    padding-bottom: 4px;
    border-bottom: 1px solid var(--rule-grey);
  }
  .rule { position: absolute; height: 1px; background: var(--rule-grey); }
  .rule-top { left: 38px; top: 118px; width: 464px; }
  .rule-name { left: 38px; top: 206px; width: 216px; }
  .person { position: absolute; left: 38px; top: 148px; }
  .person-name { font-size: 20px; font-weight: 600; color: var(--kestrel); }
  .person-title { font-size: 13px; color: var(--ink-grey); margin-top: 2px; }
  .address {
    position: absolute; left: 38px; top: 250px;
    font-size: 14px; line-height: 1.45; color: var(--ink-grey);
  }
  .contacts {
    position: absolute; left: 290px; top: 134px;
    list-style: none;
  }
  .contacts li {
    display: flex; align-items: center; gap: 9px;
    font-size: 13px; line-height: 20px; color: var(--ink-grey);
  }
  .contacts svg { width: 12px; height: 12px; fill: var(--kestrel); flex: none; }

  /* ---------- Back ---------- */
  .card-back {
    left: 610px;
    background: linear-gradient(135deg, var(--kestrel-light) 0%, var(--kestrel) 55%, var(--kestrel-deep) 100%);
  }
  .back-motif {
    position: absolute; right: -70px; top: 10px;
    width: 330px; height: 330px; border-radius: 50%;
    border: 26px solid rgba(255,255,255,0.06);
  }
  .back-brand {
    position: absolute; left: 34px; top: 92px;
    display: flex; align-items: center; gap: 16px;
  }
  .back-brand .brand-dot { border-color: var(--white); width: 54px; height: 54px; }
  .back-brand .brand-name {
    font-size: 40px; font-weight: 400; color: var(--white);
    letter-spacing: -0.4px;
    padding-bottom: 6px;
    border-bottom: 1.5px solid var(--white);
  }
  .taglines {
    position: absolute; left: 34px; bottom: 34px;
    font-size: 13px; letter-spacing: 3.4px; text-transform: uppercase;
    color: var(--white);
  }
  .taglines .divider { margin: 0 14px; }
</style>
</head>
<body>

  <section class="card card-front" aria-label="Business card front">
    <div class="front-brand">
      <span class="brand-dot"></span>
      <span class="brand-name">The Kestrel Group</span>
    </div>
    <div class="rule rule-top"></div>

    <div class="person">
      <p class="person-name">Everett Lane</p>
      <p class="person-title">manager</p>
    </div>
    <div class="rule rule-name"></div>

    <p class="address">PO Box 5817,<br>Brindlevale Qld 4178</p>

    <ul class="contacts">
      <li>
        <svg viewBox="0 0 12 12" aria-hidden="true"><rect x="1" y="4" width="10" height="7" rx="1"/><rect x="3" y="1" width="6" height="4"/></svg>
        1300 482917
      </li>
      <li>
        <svg viewBox="0 0 12 12" aria-hidden="true"><rect x="1" y="5" width="10" height="6" rx="1"/><rect x="3" y="1" width="6" height="5" fill-opacity="0.6"/></svg>
        1300 482915
      </li>
      <li>
        <svg viewBox="0 0 12 12" aria-hidden="true"><rect x="3" y="0.5" width="6" height="11" rx="1"/><rect x="4" y="2" width="4" height="6" fill="#f6f7f8"/></svg>
        0417 593 824
      </li>
      <li>
        <svg viewBox="0 0 12 12" aria-hidden="true"><rect x="0.5" y="2.5" width="11" height="7"/><path d="M0.5 2.5 L6 7 L11.5 2.5" fill="none" stroke="#f6f7f8" stroke-width="1"/></svg>
        admin@kestrelgroup-example.com.au
      </li>
      <li>
        <svg viewBox="0 0 12 12" aria-hidden="true"><rect x="1" y="6" width="2" height="5"/><rect x="4" y="4" width="2" height="7"/><rect x="7" y="7" width="2" height="4"/><rect x="0" y="11" width="12" height="1"/></svg>
        www.kestrelgroup-example.com.au
      </li>
    </ul>
  </section>

  <section class="card card-back" aria-label="Business card back">
    <div class="back-motif"></div>
    <div class="back-brand">
      <span class="brand-dot"></span>
      <span class="brand-name">The Kestrel Group</span>
    </div>
    <p class="taglines">Property Development<span class="divider">|</span>Premium Accommodation</p>
  </section>

</body>
</html>
```